Human Resource Consulting Powerpoint / Word Templates

We need Powerpoint and Word templates to use the same style as our new website. We use Powerpoint and Word when presenting to our clients. These must look professional.
- Proposal template for Powerpoint (8 Page layouts see attached)
- Presentation template for Powerpoint (8 Page layouts see attached)
- Letter head ( 1 page)
- Proposal Template for Word
- Report Template for Word
Theses should include a mini style guide including font size, text positioning on the page and image positioning.
Link to website under construction: http://www.brivaplex.com.au.42.morlatin.pw/
Our new biz card designs and logo file attached.
Consulting
- Helvetica Nue

```html
<!DOCTYPE html>
<html lang="en">
<head>
<meta charset="utf-8">
<title>Brivaplex HR – Presentation Template Layouts</title>
<link href="https://fonts.googleapis.com/css2?family=Open+Sans:wght@400;600;700&display=swap" rel="stylesheet">
<style>
:root{
  --blue:#1a8ad4;
  --blue-dark:#0f6fb0;
  --ink:#333a40;
  --grey:#6d737a;
  --line:#d9dde1;
  --slate:#5c7187;
  --charcoal:#3b3f44;
  --rock-top:#6d7988;
  --rock-bottom:#1f262e;
  --placeholder:#c4c8cc;
}
*{box-sizing:border-box;margin:0;padding:0}
html,body{width:1200px;height:1142px;overflow:hidden;background:#fff;font-family:"Open Sans",Arial,sans-serif;color:var(--ink)}
.board{position:relative;width:1200px;height:1142px}
.slide{position:absolute;width:296px;height:222px;background:#fff;overflow:hidden;box-shadow:0 0 0 1px #e3e6e9,0 1px 3px rgba(0,0,0,.12)}
.c1{left:2px}.c2{left:302px}.c3{left:602px}.c4{left:902px}
.r1{top:4px}.r2{top:231px}.r3{top:458px}.r4{top:685px}.r5{top:912px}
.abs{position:absolute}
.photo{position:absolute;background:linear-gradient(170deg,var(--rock-top) 0%,#404b57 45%,var(--rock-bottom) 100%)}
.brand{position:absolute;top:10px;right:8px;display:flex;align-items:center;gap:3px;font-size:7px;font-weight:600;color:var(--ink);letter-spacing:.2px}
.brand i{display:block;width:11px;height:11px;border-radius:50%;border:1.5px solid var(--blue);background:#fff}
.brand.light{color:#fff}
.brand.left{left:8px;right:auto}
.bankmark{position:absolute;top:12px;left:8px;font-size:9px;font-weight:700;color:var(--blue)}
.pg{position:absolute;right:6px;bottom:6px;width:11px;height:11px;border-radius:50%;background:var(--blue);color:#fff;font-size:5.5px;line-height:11px;text-align:center}
.vdots{position:absolute;left:7px;top:10px;display:flex;flex-direction:column;gap:2px}
.vdots b,.hdots b{display:block;width:4px;height:4px;border-radius:50%;border:1px solid var(--blue)}
.vdots b.on,.hdots b.on{background:var(--slate);border-color:var(--slate)}
.hdots{position:absolute;bottom:9px;right:20px;display:flex;gap:2px}
.title{position:absolute;font-size:13px;color:var(--blue);font-weight:400}
.body{font-size:5px;line-height:1.45;color:var(--grey)}
.body p{margin-bottom:5px}
.num{display:inline-block;width:12px;height:12px;border-radius:50%;background:var(--blue);color:#fff;font-size:5px;line-height:12px;text-align:center;box-shadow:0 0 0 1.5px #fff,0 0 0 2.5px var(--blue);margin-right:6px}
.list{position:absolute;font-size:6px;color:var(--ink)}
.list div{display:flex;align-items:center;height:25px}
.badge{position:absolute;width:30px;height:30px;border-radius:50%;background:var(--blue);color:#fff;font-size:5.5px;line-height:1.1;display:flex;align-items:center;justify-content:center;text-align:center;box-shadow:0 0 0 2px #fff,0 0 0 3px var(--blue)}
.hero{position:absolute;left:150px;top:80px;width:146px;height:60px;background:rgba(26,138,212,.55);color:#fff;padding:9px 14px}
.hero h1{font-size:17px;font-weight:400;line-height:1}
.hero h2{font-size:8px;font-weight:400;margin-top:2px}
.hero small{font-size:5px}
.footbar{position:absolute;left:0;right:0;bottom:0;height:24px;background:rgba(20,26,32,.6);color:#fff;display:flex;align-items:center;padding:0 8px;font-size:7px}
.person{display:flex;align-items:center;gap:4px}
.person i{width:9px;height:9px;border-radius:50%;background:var(--blue);display:block}
.person small{display:block;font-size:4.5px;color:#57aee8}
.clients{position:absolute;left:12px;top:52px;width:272px;height:124px;background:#fff;text-align:center}
.clients h3{font-size:12px;font-weight:400;color:var(--blue);margin-top:8px}
.clients p{font-size:5.5px;color:var(--grey)}
.cgrid{display:grid;grid-template-columns:repeat(5,1fr);margin:8px 6px 0}
.cgrid span{height:34px;display:flex;align-items:center;justify-content:center;font-size:6px;font-weight:600;color:var(--charcoal);border-right:1px solid #eef0f2;border-bottom:1px solid #eef0f2}
.help{position:absolute;top:64px;width:46px}
.help .ph{height:46px;position:relative}
.help h4{font-size:4.8px;color:var(--blue);font-weight:400;margin-top:11px;line-height:1.3}
.help p{font-size:4.5px;color:var(--grey);margin-top:6px;line-height:1.4}
.col3{position:absolute;top:62px;width:86px;text-align:center}
.col3 .ic{width:32px;height:32px;margin:0 auto;border-radius:50%;background:var(--blue);box-shadow:0 0 0 2px #fff,0 0 0 3px var(--blue);display:flex;align-items:center;justify-content:center}
.col3 h4{font-size:6px;color:var(--blue);font-weight:600;margin-top:14px}
.col3 p{font-size:4.8px;color:var(--grey);line-height:1.45;margin-top:5px}
.fees{position:absolute;left:12px;top:54px;width:274px;height:138px;box-shadow:0 1px 4px rgba(0,0,0,.2);display:grid;grid-template-columns:108px 82px 84px;font-size:4.5px}
.fees .h{height:34px;color:#fff;font-weight:600;padding:8px 4px;font-size:5px;text-align:center}
.fees .rows div{height:9px;border-bottom:1px solid var(--line);margin:0 6px;display:flex;align-items:center;justify-content:center}
.fees .desc div{justify-content:flex-start}
.fees .ico{width:18px;height:18px;border-radius:50%;background:#fff;margin:3px auto 0;border:1px solid var(--line)}
.contact-row{display:flex;align-items:center;font-size:5.5px;height:12px;color:var(--ink)}
.contact-row i{width:7px;height:7px;border-radius:50%;background:var(--blue);margin-right:7px}
.contact-row b{font-weight:400;width:28px}
.contact-row em{font-style:normal;width:10px}
.step-label{position:absolute;font-size:6px;color:var(--blue);font-weight:600}
.quote-mark{position:absolute;font-size:26px;line-height:1;color:var(--slate);font-style:italic;font-weight:700}
</style>
</head>
<body>
<div class="board">

<!-- Row 1 -->
<section class="slide c1 r1">
  <div class="bankmark">Harbourline Bank</div>
  <div class="brand"><i></i>BRIVAPLEX</div>
  <div class="photo" style="left:0;top:36px;width:296px;height:186px" role="img" aria-label="Snow-covered mountain range photograph"></div>
  <div class="hero"><h1>Proposal</h1><h2>Corporation</h2><small>July 1, 2016</small></div>
  <div class="footbar">
    <span style="font-size:5px;margin-right:4px">For</span>
    <div class="person"><i></i><div>Dane Ostrow<small>Vice President</small></div></div>
    <span style="font-size:5px;margin:0 4px 0 auto">From</span>
    <div class="person"><i></i><div>Mira Kellaway<small>Director of Consulting</small></div></div>
  </div>
</section>

<section class="slide c2 r1">
  <div class="bankmark">Harbourline Bank</div>
  <div class="brand"><i></i>BRIVAPLEX</div>
  <div class="photo" style="left:0;top:36px;width:296px;height:186px" role="img" aria-label="Snow-covered mountain range photograph"></div>
  <div class="hero"><h1>Presentation</h1><h2>Subtitle here</h2><small>August 1, 2016</small></div>
  <div class="footbar">
    <div class="person"><i></i><div>Mira Kellaway<small>Director of Consulting</small></div></div>
  </div>
</section>

<section class="slide c3 r1">
  <div class="vdots"><b></b><b></b><b></b><b></b><b></b><b></b><b></b><b></b><b></b></div>
  <div class="brand"><i></i>BRIVAPLEX</div>
  <div class="title" style="left:18px;top:13px">Content</div>
  <div class="list" style="left:46px;top:60px">
    <div><span class="num">1</span>Content No. 1</div><div><span class="num">2</span>Content No. 2</div><div><span class="num">3</span>Content No. 3</div><div><span class="num">4</span>Content No. 4</div><div><span class="num">5</span>Content No. 5</div>
  </div>
  <div class="list" style="left:168px;top:60px">
    <div><span class="num">6</span>Content No. 6</div><div><span class="num">7</span>Content No. 7</div><div><span class="num">8</span>Content No. 8</div><div><span class="num">9</span>Content No. 9</div><div><span class="num">10</span>Content No. 10</div>
  </div>
  <div class="pg">3</div>
</section>

<section class="slide c4 r1">
  <div class="vdots"><b></b><b></b><b></b><b></b><b></b><b></b><b></b><b></b><b></b></div>
  <div class="photo" style="left:146px;top:0;width:150px;height:222px" role="img" aria-label="Mountain peak photograph"></div>
  <div class="brand light"><i></i>BRIVAPLEX</div>
  <div class="title" style="left:18px;top:13px">Large Image Right</div>
  <div class="body abs" style="left:18px;top:62px;width:108px">
    <p>Brivaplex HR is a human resource consultancy transforming businesses all over Australia. We combine HR and Strategy to create the momentum behind great businesses.</p>
    <p>We believe that people are at the heart of every great business. To achieve real growth, businesses need to continuously refine the way they measure, manage and motivate their people.</p>
    <p>We refer to this as the Journey to Greatness and pride ourselves in taking businesses on this journey so they can achieve great things.</p>
  </div>
  <div class="badge" style="left:133px;top:96px">Your<br>Text</div>
  <div class="pg">4</div>
</section>

<!-- Row 2 -->
<section class="slide c1 r2">
  <div class="vdots"><b></b><b></b><b></b><b></b><b></b><b></b><b></b><b></b><b></b></div>
  <div class="brand"><i></i>BRIVAPLEX</div>
  <div class="abs" style="left:18px;top:86px;width:90px;height:100px;background:var(--placeholder)" role="img" aria-label="Feature photograph placeholder"></div>
  <div class="title" style="left:130px;top:58px">Image Left</div>
  <div class="body abs" style="left:130px;top:86px;width:150px">
    <p>Brivaplex HR is a human resource consultancy transforming businesses all over Australia. We combine HR and Strategy to create the momentum behind great businesses.</p>
    <p>We believe that people are at the heart of every great business. To achieve real growth, businesses need to continuously refine the way they measure, manage and motivate their people.</p>
    <p>We refer to this as the Journey to Greatness and pride ourselves in taking businesses on this journey so they can achieve great things.</p>
  </div>
  <div class="pg">5</div>
</section>

<section class="slide c2 r2">
  <div class="photo" style="left:0;top:0;width:296px;height:152px" role="img" aria-label="Snow-covered mountain range photograph"></div>
  <div class="brand left light"><i></i>BRIVAPLEX</div>
  <div class="badge" style="left:20px;top:136px">Your<br>Text</div>
  <div class="body abs" style="left:16px;top:168px;width:270px;text-indent:40px">Brivaplex HR is a human resource consultancy transforming businesses all over Australia. We combine HR and Strategy to create the momentum behind great businesses.</div>
  <div class="body abs" style="left:16px;top:186px;width:270px">We believe that people are at the heart of every great business.<br>To achieve real growth, businesses need to continuously refine the way they measure, manage and motivate their people.</div>
  <div class="hdots"><b></b><b></b><b class="on"></b><b class="on"></b><b></b><b class="on"></b><b></b><b></b><b></b></div>
  <div class="pg">6</div>
</section>

<section class="slide c3 r2">
  <div class="brand left"><i></i>BRIVAPLEX</div>
  <div class="title" style="left:0;width:296px;text-align:center;top:42px">Heading &amp; Text</div>
  <div class="body abs" style="left:26px;top:78px;width:244px;text-align:center">
    <p>Brivaplex HR is a human resource consultancy transforming businesses all over Australia. We combine HR and Strategy to create the momentum behind great businesses.</p>
    <p style="margin-top:10px">We believe that people are at the heart of every great business. To achieve real growth, businesses need to continuously refine the way they measure, manage and motivate their people.</p>
    <p style="margin-top:10px">We refer to this as the Journey to Greatness and pride ourselves in taking businesses on this journey so they can achieve great things.</p>
  </div>
  <div class="hdots"><b class="on"></b><b></b><b class="on"></b><b></b><b></b><b></b><b></b><b></b><b></b></div>
  <div class="pg">7</div>
</section>

<section class="slide c4 r2">
  <div class="brand left"><i></i>BRIVAPLEX</div>
  <div class="abs" style="left:132px;top:64px;width:32px;height:32px;border-radius:50%;background:var(--blue);box-shadow:0 0 0 2px #fff,0 0 0 3px var(--blue);color:#fff;font-size:22px;font-weight:700;text-align:center;line-height:40px">&ldquo;</div>
  <div class="quote-mark" style="left:36px;top:98px">&ldquo;</div>
  <div class="abs" style="left:46px;top:108px;width:220px;text-align:center;font-size:7.5px;line-height:1.5;color:var(--ink)">It is not the strongest of the species that survives,<br>nor the most intelligent that survives.<br>It is the one that is most adaptable to change.</div>
  <div class="abs" style="left:0;width:296px;top:148px;text-align:center;font-size:5px;color:var(--blue)">- Leon Farrow -</div>
  <div class="quote-mark" style="left:248px;top:136px">&rdquo;</div>
  <div class="hdots"><b></b><b></b><b></b><b class="on"></b><b></b><b></b><b></b><b></b><b></b></div>
  <div class="pg">8</div>
</section>

<!-- Row 3 -->
<section class="slide c1 r3">
  <div class="vdots"><b></b><b></b><b></b><b></b><b></b><b></b><b></b><b></b><b></b></div>
  <div class="brand"><i></i>BRIVAPLEX</div>
  <div class="title" style="left:18px;top:13px">Bullet Area</div>
  <div class="abs" style="left:0;top:150px;width:100px;height:72px;background:var(--placeholder)" role="img" aria-label="Photograph of a businessman's outstretched hand"></div>
  <div class="list" style="left:114px;top:52px">
    <div><span class="num">1</span>Bullets and Numbering 1</div><div><span class="num">2</span>Bullets and Numbering 2</div><div><span class="num">3</span>Bullets and Numbering 3</div><div><span class="num">4</span>Bullets and Numbering 4</div><div><span class="num">5</span>Bullets and Numbering 5</div><div><span class="num">6</span>Bullets and Numbering 6</div>
  </div>
  <div class="pg">9</div>
</section>

<section class="slide c2 r3">
  <div class="photo" style="left:0;top:0;width:296px;height:222px" role="img" aria-label="Snow-covered mountain range photograph"></div>
  <div class="brand left light"><i></i>BRIVAPLEX</div>
  <div class="abs" style="left:14px;top:52px;width:268px;height:124px;background:#fff">
    <div style="position:absolute;left:12px;top:10px;font-size:8px;color:var(--blue)">Special Offer</div>
    <div class="body abs" style="left:12px;top:28px;width:130px">
      <p>&bull; Brivaplex HR is a human resource consultancy transforming businesses all over Australia. We combine HR and Strategy to create the momentum behind great businesses.</p>
      <p>&bull; We believe that people are at the heart of every great business. To achieve real growth, businesses need to continuously refine the way they measure, manage and motivate their people.</p>
    </div>
    <div class="abs" style="left:156px;top:28px;width:100px;height:66px;border:2px solid var(--slate);border-radius:4px;background:linear-gradient(135deg,#9aa6b2,#2e3946)" role="img" aria-label="Photograph of team hands joined together"></div>
    <div class="hdots" style="bottom:10px;right:10px"><b></b><b class="on"></b><b></b><b></b><b></b><b></b><b></b><b></b><b></b></div>
  </div>
  <div class="pg">10</div>
</section>

<section class="slide c3 r3">
  <div class="brand"><i></i>BRIVAPLEX</div>
  <div class="title" style="left:12px;top:16px">Brivaplex</div>
  <div class="body abs" style="left:12px;top:62px;width:84px;font-size:4.6px">
    <p>Brivaplex HR is a human resource consultancy transforming businesses all over Australia. We combine HR and Strategy to create the momentum behind great businesses.</p>
    <p>We believe that people are at the heart of every great business. To achieve real growth, businesses need to continuously refine the way they measure, manage and motivate their people.</p>
    <p>We refer to this as the Journey to Greatness and pride ourselves in taking businesses on this journey so they can achieve great things.</p>
  </div>
  <div class="abs" style="left:97px;top:60px;width:98px;height:162px;background:linear-gradient(180deg,#7e91a5,#4f6275 60%,#2f3c4a)" role="img" aria-label="Photograph of a lighthouse at dusk"></div>
  <div class="body abs" style="left:205px;top:62px;width:80px;font-size:4.6px">
    <p>Brivaplex HR is a human resource consultancy transforming businesses all over Australia. We combine HR and Strategy to create the momentum behind great businesses.</p>
    <p>We believe that people are at the heart of every great business. To achieve real growth, businesses need to continuously refine the way they measure, manage and motivate their people.</p>
    <p>We refer to this as the Journey to Greatness and pride ourselves in taking businesses on this journey so they can achieve great things.</p>
  </div>
  <div class="hdots"><b class="on"></b><b></b><b></b><b class="on"></b><b></b><b></b><b></b><b></b><b></b></div>
  <div class="pg">11</div>
</section>

<section class="slide c4 r3">
  <div class="photo" style="left:0;top:0;width:296px;height:222px" role="img" aria-label="Snow-covered mountain range photograph"></div>
  <div class="brand left light"><i></i>BRIVAPLEX</div>
  <div class="clients">
    <h3>Our Clients</h3>
    <p>We work across all industries</p>
    <div class="cgrid">
      <span>Harbourline Bank</span><span>Kestrel Systems</span><span>Varno</span><span>Pellway</span><span>Northmere Council</span>
      <span>Ashgrove Funerals</span><span>Quillon</span><span>Tanberg Group</span><span>Marrow &amp; Finch</span><span>Cleanfield Lab</span>
    </div>
  </div>
  <div class="hdots" style="bottom:48px;right:18px"><b></b><b></b><b class="on"></b><b></b><b></b><b></b><b></b><b></b><b></b></div>
  <div class="pg">12</div>
</section>

<!-- Row 4 -->
<section class="slide c1 r4">
  <div class="vdots"><b></b><b></b><b></b><b></b><b></b><b></b><b></b><b></b><b></b></div>
  <div class="brand"><i></i>BRIVAPLEX</div>
  <div class="title" style="left:18px;top:13px">Chart Area</div>
  <div class="body abs" style="left:34px;top:46px;width:230px">&bull; Brivaplex HR is a human resource consultancy transforming businesses all over Australia. We combine HR and Strategy to create the momentum behind great businesses.</div>
  <div class="abs" style="left:48px;top:100px;font-size:5px;color:var(--grey)">
    <div style="display:flex;align-items:center;height:29px"><i style="width:11px;height:11px;border-radius:50%;background:var(--blue);margin-right:5px;display:block"></i>Category 1<span style="font-size:12px;color:var(--blue);margin-left:8px">60%</span></div>
    <div style="display:flex;align-items:center;height:29px"><i style="width:11px;height:11px;border-radius:50%;background:var(--slate);margin-right:5px;display:block"></i>Category 2<span style="font-size:12px;color:var(--slate);margin-left:8px">30%</span></div>
    <div style="display:flex;align-items:center;height:29px"><i style="width:11px;height:11px;border-radius:50%;background:var(--charcoal);margin-right:5px;display:block"></i>Category 3<span style="font-size:12px;color:var(--charcoal);margin-left:8px">10%</span></div>
  </div>
  <svg class="abs" style="left:158px;top:100px" width="80" height="80" viewBox="0 0 80 80">
    <g transform="rotate(-90 40 40)" fill="none" stroke-width="6">
      <circle cx="40" cy="40" r="36" stroke="var(--charcoal)"/>
      <circle cx="40" cy="40" r="36" stroke="var(--slate)" stroke-dasharray="203.6 226.2"/>
      <circle cx="40" cy="40" r="36" stroke="var(--blue)" stroke-dasharray="135.7 226.2" transform="rotate(108 40 40)"/>
    </g>
    <text x="40" y="44" text-anchor="middle" font-family="Open Sans, sans-serif" font-size="12" fill="#6d737a">Chart</text>
  </svg>
  <div class="pg">13</div>
</section>

<section class="slide c2 r4">
  <div class="brand"><i></i>BRIVAPLEX</div>
  <div class="title" style="left:18px;top:13px">How we help our clients</div>
  <div class="help" style="left:12px"><div class="ph photo" style="position:relative" role="img" aria-label="Rocky mountain photograph"></div><h4>The Foundations of Greatness</h4><p>We provide advice, policies &amp; templates to keep you compliant</p></div>
  <div class="help" style="left:68px"><div class="ph photo" style="position:relative" role="img" aria-label="Lighthouse photograph"></div><h4>The Heart of Greatness</h4><p>We set you up with the critical people systems that sit at the core of great business</p></div>
  <div class="help" style="left:125px"><div class="ph photo" style="position:relative" role="img" aria-label="Dark landscape photograph"></div><h4>Resourcing Greatness</h4><p>We ensure you can attract and hire the right people to maintain your momentum</p></div>
  <div class="help" style="left:182px"><div class="ph photo" style="position:relative" role="img" aria-label="Climber photograph"></div><h4>Developing Greatness</h4><p>We ensure you have star players and star teams at all levels</p></div>
  <div class="help" style="left:239px"><div class="ph photo" style="position:relative" role="img" aria-label="Summit flag photograph"></div><h4>Embedding Greatness</h4><p>We embed HR Specialists in your business to power your momentum</p></div>
  <div class="hdots"><b></b><b></b><b class="on"></b><b class="on"></b><b></b><b class="on"></b><b></b><b></b><b></b></div>
  <div class="pg">14</div>
</section>

<section class="slide c3 r4">
  <div class="vdots"><b></b><b></b><b></b><b></b><b></b><b></b><b></b><b></b><b></b></div>
  <div class="brand"><i></i>BRIVAPLEX</div>
  <div class="title" style="left:0;width:296px;text-align:center;top:25px">3 Column Area</div>
  <div class="abs" style="left:100px;top:55px;width:1px;height:145px;background:var(--line)"></div>
  <div class="abs" style="left:195px;top:55px;width:1px;height:145px;background:var(--line)"></div>
  <div class="col3" style="left:10px"><div class="ic"><svg width="16" height="16" viewBox="0 0 16 16"><path d="M10 1 4 9h4l-2 6 6-8H8z" fill="#fff"/></svg></div><h4>Column 1</h4><p>Brivaplex HR is a human resource consultancy transforming businesses all over Australia. We combine HR and Strategy to create the momentum behind great businesses.</p></div>
  <div class="col3" style="left:105px"><div class="ic"><svg width="16" height="16" viewBox="0 0 16 16"><circle cx="8" cy="8" r="3.5" fill="#fff"/><g stroke="#fff" stroke-width="1.2"><path d="M8 0v2.5M8 13.5V16M0 8h2.5M13.5 8H16M2.3 2.3l1.8 1.8M11.9 11.9l1.8 1.8M2.3 13.7l1.8-1.8M11.9 4.1l1.8-1.8"/></g></svg></div><h4>Column 2</h4><p>Brivaplex HR is a human resource consultancy transforming businesses all over Australia. We combine HR and Strategy to create the momentum behind great businesses.</p></div>
  <div class="col3" style="left:200px"><div class="ic"><svg width="16" height="16" viewBox="0 0 16 16"><path d="M3 1h10L8 8l5 7H3l5-7z" fill="#fff"/></svg></div><h4>Column 3</h4><p>Brivaplex HR is a human resource consultancy transforming businesses all over Australia. We combine HR and Strategy to create the momentum behind great businesses.</p></div>
  <div class="pg">15</div>
</section>

<section class="slide c4 r4">
  <div class="brand"><i></i>BRIVAPLEX</div>
  <div class="title" style="left:18px;top:15px">Professional Fees</div>
  <div class="fees">
    <div><div class="h" style="background:var(--blue);text-align:left">Description</div>
      <div class="rows desc" style="margin-top:16px;color:var(--grey)"><div>Description 1</div><div>Description 2</div><div>Description 3</div><div>Description 4</div><div>Description 5</div><div>Description 6</div><div>Description 7</div><div>Description 8</div></div></div>
    <div><div class="h" style="background:var(--slate)">Column 1<div class="ico"></div></div>
      <div class="rows" style="margin-top:16px"><div>&#9679;</div><div>&#9679;</div><div>-</div><div>&#9679;</div><div>Text Column 1</div><div>-</div><div>Text Column 1</div><div>&#9679;</div></div></div>
    <div><div class="h" style="background:var(--charcoal)">Column 2<div class="ico"></div></div>
      <div class="rows" style="margin-top:16px"><div>&#9679;</div><div>&#9679;</div><div>&#9679;</div><div>&#9679;</div><div>Text Column 2</div><div>-</div><div>Text Column 2</div><div>&#9679;</div></div></div>
  </div>
  <div class="hdots"><b></b><b></b><b class="on"></b><b></b><b class="on"></b><b></b><b></b><b></b><b></b></div>
  <div class="pg">16</div>
</section>

<!-- Row 5 -->
<section class="slide c1 r5">
  <div class="vdots"><b></b><b></b><b></b><b></b><b></b><b></b><b></b><b></b><b></b></div>
  <div class="brand"><i></i>BRIVAPLEX</div>
  <div class="title" style="left:18px;top:13px">Steps Area</div>
  <svg class="abs" style="left:0;top:0" width="296" height="222" viewBox="0 0 296 222">
    <g stroke="var(--blue)" stroke-width="0.8" fill="none">
      <path d="M146 58v16M146 90v16M72 106h146M72 106v16M218 106v16"/>
      <path d="M64 134q-10 5-12 15M226 134q10 5 12 15"/>
    </g>
    <g fill="var(--blue)"><circle cx="72" cy="106" r="2.2"/><circle cx="146" cy="106" r="2.2"/><circle cx="218" cy="106" r="2.2"/><path d="M146 55l-2 4h4z"/><path d="M50 148l2 4 2-4z"/><path d="M236 148l2 4 2-4z"/></g>
  </svg>
  <div class="badge" style="left:138px;top:74px;width:16px;height:16px;font-size:6px">2</div>
  <div class="badge" style="left:64px;top:122px;width:16px;height:16px;font-size:6px">1</div>
  <div class="badge" style="left:210px;top:122px;width:16px;height:16px;font-size:6px">3</div>
  <div class="step-label" style="left:138px;top:18px">Step 2</div>
  <div class="body abs" style="left:96px;top:26px;width:104px;text-align:center">Brivaplex HR is a human resource consultancy transforming businesses all over Australia.</div>
  <div class="step-label" style="left:31px;top:153px">Step 1</div>
  <div class="body abs" style="left:30px;top:161px;width:96px;text-align:center">Brivaplex HR is a human resource consultancy transforming businesses all over Australia. We combine HR and Strategy to create the momentum behind great businesses.</div>
  <div class="step-label" style="left:240px;top:153px">Step 3</div>
  <div class="body abs" style="left:166px;top:161px;width:96px;text-align:center">Brivaplex HR is a human resource consultancy transforming businesses all over Australia. We combine HR and Strategy to create the momentum behind great businesses.</div>
  <div class="pg">17</div>
</section>

<section class="slide c2 r5">
  <div class="brand"><i></i>BRIVAPLEX</div>
  <div class="title" style="left:18px;top:13px">Contact</div>
  <div class="abs" style="left:20px;top:72px;width:78px;height:78px;border:2px solid #c9cdd1;border-radius:4px;background:var(--placeholder)" role="img" aria-label="Portrait photograph of Mira Kellaway"></div>
  <div class="abs" style="left:106px;top:74px;font-size:13px;color:var(--blue)">Mira Kellaway</div>
  <div class="abs" style="left:106px;top:93px;font-size:6.5px;color:var(--ink)">Director of Consulting</div>
  <div class="abs" style="left:106px;top:104px">
    <div class="contact-row"><i></i><b>Email</b><em>:</em>info@brivaplexhr.com.au</div>
    <div class="contact-row"><i></i><b>Website</b><em>:</em>www.brivaplex.com.au.42.morlatin.pw</div>
    <div class="contact-row"><i></i><b>Phone</b><em>:</em>1300 48 2716</div>
    <div class="contact-row"><i></i><b>Linkedin</b><em>:</em>linkedin.com/mirakellaway</div>
  </div>
  <div class="hdots"><b></b><b></b><b></b><b></b><b></b><b></b><b></b><b></b><b class="on"></b></div>
  <div class="pg">18</div>
</section>

<section class="slide c3 r5">
  <div class="photo" style="left:0;top:0;width:296px;height:222px" role="img" aria-label="Snow-covered mountain range photograph"></div>
  <div class="abs" style="left:28px;top:76px;font-size:22px;color:#fff">Thank You</div>
  <div class="abs" style="left:42px;top:104px;font-size:6px;color:var(--blue)">For your precious time</div>
  <div class="abs" style="left:0;right:0;bottom:0;height:44px;background:rgba(20,26,32,.55);color:#fff;font-size:5px">
    <div style="position:absolute;left:8px;top:6px;line-height:11px">
      <div class="person"><i style="width:7px;height:7px"></i>1300 48 2716</div>
      <div class="person"><i style="width:7px;height:7px"></i>info@brivaplexhr.com.au</div>
      <div class="person"><i style="width:7px;height:7px"></i>www.brivaplex.com.au.42.morlatin.pw</div>
    </div>
    <div class="person" style="position:absolute;left:188px;top:8px;align-items:flex-start"><i style="width:7px;height:7px"></i><div style="line-height:1.4">Brivaplex Pty Ltd<br>Head Office<br>Level 14, Corvin Tower - 9 Lanner Street<br>Sydney NSW 2000</div></div>
  </div>
</section>

</div>
</body>
</html>
```